Need a book cover design for book titled: Resting Beside the River--Simple Methods for the Crossing

This book describes and presents tools to connect with and activate the Lightbody that we all carry within us. It talks about the Lighbody, brief history, lightbody levels and offers exercises to bring light into the body.
I envision a design that shows a physical body changing into light /surrounded by light; a resurrected body ascending to higher dimensions of Spirit o anything comparable .
Updates

Target Market(s)

Mature audience of spiritual seekers and those on spiritual path

Requirements
Must have
• Space on backcover for book summary at top and title and author name on spine.

```html
<!DOCTYPE html>
<html lang="en">
<head>
<meta charset="utf-8">
<title>Resting Beside the River — Book Cover</title>
<link rel="stylesheet" href="https://fonts.googleapis.com/css2?family=Anton&family=Cinzel:wght@400&family=Inter:wght@300;400&display=swap">
<style>
  :root {
    --stage: #8a8a8a;
    --cover-deep: #161b3c;
    --cover-glow: #0b4a92;
    --type-light: #f4f4f6;
  }
  html, body {
    margin: 0;
    padding: 0;
    width: 1200px;
    height: 1200px;
    overflow: hidden;
    background: var(--stage);
  }
  .book-cover {
    position: absolute;
    left: 250px;
    top: 66px;
    width: 700px;
    height: 1068px;
    overflow: hidden;
    background:
      radial-gradient(ellipse 60% 45% at 50% 42%, var(--cover-glow) 0%, rgba(11,74,146,0.35) 45%, rgba(22,27,60,0) 80%),
      var(--cover-deep);
  }
  .subtitle {
    position: absolute;
    top: 46px;
    left: 0;
    width: 100%;
    margin: 0;
    text-align: center;
    font-family: "Inter", Helvetica, Arial, sans-serif;
    font-weight: 400;
    font-size: 33px;
    letter-spacing: -0.2px;
    color: var(--type-light);
  }
  .title-art {
    position: absolute;
    left: 0;
    top: 0;
    width: 700px;
    height: 1068px;
  }
  .title-word {
    font-family: "Anton", "Impact", sans-serif;
  }
  .author-name {
    position: absolute;
    top: 998px;
    left: 0;
    width: 100%;
    margin: 0;
    text-align: center;
    font-family: "Cinzel", "Trajan Pro", serif;
    font-weight: 400;
    font-size: 47px;
    letter-spacing: 1px;
    color: var(--type-light);
  }
</style>
</head>
<body>
  <main class="book-cover">
    <p class="subtitle">Simple Methods for the Crossing</p>

    <svg class="title-art" viewBox="0 0 700 1068" xmlns="http://www.w3.org/2000/svg">
      <defs>
        <linearGradient id="spectrum" gradientUnits="userSpaceOnUse" x1="0" y1="140" x2="0" y2="960">
          <stop offset="0" stop-color="#d763b4"/>
          <stop offset="0.13" stop-color="#e9a6d6"/>
          <stop offset="0.22" stop-color="#5a5bb8"/>
          <stop offset="0.34" stop-color="#1fb4dc"/>
          <stop offset="0.48" stop-color="#17a894"/>
          <stop offset="0.62" stop-color="#6fc23c"/>
          <stop offset="0.74" stop-color="#d2c21e"/>
          <stop offset="0.88" stop-color="#ec9aa0"/>
          <stop offset="1" stop-color="#e21d2c"/>
        </linearGradient>
        <linearGradient id="edge-fade" gradientUnits="userSpaceOnUse" x1="0" y1="0" x2="700" y2="0">
          <stop offset="0" stop-color="#2a3aa6" stop-opacity="0.9"/>
          <stop offset="0.3" stop-color="#2a3aa6" stop-opacity="0"/>
          <stop offset="0.7" stop-color="#2a3aa6" stop-opacity="0"/>
          <stop offset="1" stop-color="#2a3aa6" stop-opacity="0.9"/>
        </linearGradient>
        <radialGradient id="figure-glow" cx="350" cy="560" r="300" gradientUnits="userSpaceOnUse">
          <stop offset="0" stop-color="#ffffff" stop-opacity="0.45"/>
          <stop offset="0.6" stop-color="#ffffff" stop-opacity="0.15"/>
          <stop offset="1" stop-color="#ffffff" stop-opacity="0"/>
        </radialGradient>
        <clipPath id="title-shape">
          <text class="title-word" x="350" y="189" font-size="54" text-anchor="middle" textLength="223" lengthAdjust="spacingAndGlyphs">RESTING</text>
          <text class="title-word" x="350" y="281" font-size="104" text-anchor="middle" textLength="250" lengthAdjust="spacingAndGlyphs">BESIDE</text>
          <text class="title-word" x="375" y="445" font-size="182" text-anchor="middle" textLength="332" lengthAdjust="spacingAndGlyphs">THE</text>
          <text class="title-word" x="350" y="955" font-size="580" text-anchor="middle" textLength="690" lengthAdjust="spacingAndGlyphs">RIVER</text>
        </clipPath>
      </defs>

      <g class="title-lettering" clip-path="url(#title-shape)">
        <rect x="0" y="120" width="700" height="850" fill="url(#spectrum)"/>
        <rect x="0" y="120" width="700" height="850" fill="url(#edge-fade)"/>
        <rect role="img" aria-label="Glowing human figure rising upward, arms open, dissolving into rainbow light" x="0" y="120" width="700" height="850" fill="url(#figure-glow)"/>
      </g>
      <text x="-9999" y="-9999" font-size="1">Resting Beside the River</text>
    </svg>

    <p class="author-name">AUTHOR NAME</p>
  </main>
</body>
</html>
```